label for selfmade spirits, start-up, quality product

Hey there, my name is Tobias, I am 24 years old, living in the southwest of Germany. In the last two years I did experiment: I produced my own spirits. I used self-produced fruit and distilled it in my families small distillery. Distilling has been a tradition in my family, now I want to start my own production and sales. In our region distilling fruit is a tradition but it is in the hand of well-established families / producers. I am planning to establish a quality product with a modern design to focus more on younger people and to sell my spirits to bars, restaurants and private consumers. I did two varieties: "Vello plum variety" and "Mirabelle de Nancy". (Mirabelle) I am looking for a label design. The bottles will have 0.7 liters, white glass (due to the clear color of the spirits), in a modern bottle: https://www.glasbruckhaus-beispiel.de/flaschen-und-glaeser/spirituosen/spirituosenflaschen/varna-417 , html taste: clear and noble fruit character in the nose, fine flavor of the respective fruit. During the distillation process I tried to capture the natural aroma of the fruit. Therefore, I did a 2nd distilation which is a special feature, that not everybody does. Vello Zwetschgen Brand "/" Mirabelle de Nancy Brand "- I am also open for. The design can be: - simple and classy, ​​with a valuable appearance that shows in its font, which is the product itself 3 generations were involved in the production, my grandpa gave me important hints, .. I am so open for all ideas that could catch the target group. the label could be printed on either a white or cream label paper. If you have any questions don`t hesitate to contact me, I am looking forward to your suggestions! Cheers!

Target Market(s)

young adults, urban people, people with an interest in a high quality product, ars / restaurants / private customers

Font styles to use
Decorative
Script

Colors

Designer to choose colors to be used in the design.

Requirements
Must have
• So, there are some things that have been posted on the label, due to legal restrictions: - my address: Tobias Wernsdorfer, Lindenweg 14, 68412 Rebenhausen - alcohol level: "alc. 42% vol." - capacity: "0.70 L"; size at least 4 mm - batch number: "L"; please leave an empty space to fill in by hand this information has not been discussed, but should not be too much in the foreground, nor attract to much attention.

```html
<!DOCTYPE html>
<html lang="de">
<head>
<meta charset="utf-8">
<title>Vello Zwetschge Brand – Etikett</title>
<link href="https://fonts.googleapis.com/css2?family=Montserrat:wght@300;400;700&family=Oswald:wght@300&display=swap" rel="stylesheet">
<style>
  :root {
    --paper: #ffffff;
    --ink: #111111;
    --label-edge: #7a7a7a;
    --gold-solid: #b8902f;
    --gold-band: linear-gradient(90deg, #8a5c14 0%, #c9a24e 25%, #fbefb0 50%, #d8bb6a 65%, #a7822f 80%, #c4962c 90%, #8a6a10 100%);
  }
  * { margin: 0; padding: 0; box-sizing: border-box; }
  html, body { width: 1200px; height: 1200px; overflow: hidden; background: var(--paper); }
  body { font-family: "Montserrat", Arial, sans-serif; color: var(--ink); position: relative; }

  .label {
    position: absolute; left: 201px; top: 38px; width: 826px; height: 989px;
    border: 1px solid var(--label-edge); background: var(--paper);
  }
  .band { position: absolute; left: 0; right: 0; background: var(--gold-band); }
  .band--top { top: 67px; height: 12px; }
  .band--thin { top: 845px; height: 5px; }
  .band--thick { top: 862px; height: 12px; }

  .spec { position: absolute; top: 108px; font-weight: 300; font-size: 25px; letter-spacing: 0.02em; }
  .spec--abv { left: 42px; }
  .spec--volume { right: 80px; }

  .brand {
    position: absolute; left: 0; right: 46px; top: 297px; text-align: center;
    font-family: "Oswald", "Arial Narrow", sans-serif;
    font-weight: 300; font-size: 220px; line-height: 1; letter-spacing: 0.04em;
    color: var(--gold-solid);
  }
  .variety {
    position: absolute; left: 293px; top: 524px;
    font-weight: 700; font-size: 24px; letter-spacing: 0.26em; white-space: nowrap;
  }

  .producer { position: absolute; left: 0; right: 0; text-align: center; font-weight: 300; }
  .producer__name { top: 730px; font-size: 38px; letter-spacing: 0.01em; }
  .producer__address { top: 793px; font-size: 26px; letter-spacing: 0.02em; }

  .batch {
    position: absolute; left: 292px; top: 901px; width: 212px; height: 45px;
    border: 2px solid var(--ink); padding-left: 20px;
    font-weight: 700; font-size: 38px; line-height: 42px;
  }
</style>
</head>
<body>
  <main class="label">
    <div class="band band--top"></div>
    <p class="spec spec--abv">alc. 42% vol</p>
    <p class="spec spec--volume">0,70 L</p>

    <h1 class="brand">VELLO</h1>
    <p class="variety">ZWETSCHGE BRAND</p>

    <p class="producer producer__name">Tobias Wernsdorfer</p>
    <p class="producer producer__address">Lindenweg 14, 68412 Rebenhausen</p>

    <div class="band band--thin"></div>
    <div class="band band--thick"></div>
    <div class="batch">L</div>
  </main>
</body>
</html>
```